Helicopter Medical Alert

I am looking for an app that quickly displays the coordinates of where the emergency is located. Once that is displayed then the ability for the caller to call 911 and the coordinates will still be displayed on the calling screen. Two examples I have researched are Quillbenson and Tobelund. We don't have a call centre so the emergency number will solely be 911

Medical

```html
<!DOCTYPE html>
<html lang="en">
<head>
<meta charset="utf-8">
<title>Helicopter Medical Alert</title>
<link href="https://fonts.googleapis.com/css2?family=Open+Sans:wght@400;600;700&display=swap" rel="stylesheet">
<style>
  :root {
    --panel-top: #2f4f54;
    --panel-bottom: #1c3a41;
    --accent: #5cc3a6;
    --muted: #9aa9ab;
    --text-light: #f2f5f5;
    --button-border: #c9d0d1;
    --button-fill: rgba(255, 255, 255, 0.04);
    --map-land: #e9e5dc;
    --map-forest: #c9dca6;
    --alert-red: #e8453c;
  }
  * { box-sizing: border-box; margin: 0; padding: 0; }
  html, body {
    width: 743px;
    height: 1200px;
    overflow: hidden;
    background: var(--panel-bottom);
    font-family: "Open Sans", sans-serif;
  }
  .app-screen {
    position: relative;
    width: 743px;
    height: 1200px;
    overflow: hidden;
  }
  .location-panel {
    position: absolute;
    inset: 0 0 406px 0;
    background: linear-gradient(180deg, var(--panel-top) 0%, #2a4a50 55%, var(--panel-bottom) 100%);
  }
  .status-bar {
    position: absolute;
    top: 0; left: 0; right: 0;
    height: 50px;
    display: flex;
    align-items: center;
    justify-content: space-between;
    padding: 0 20px;
    color: var(--text-light);
    font-size: 24px;
  }
  .status-left, .status-right { display: flex; align-items: center; gap: 8px; width: 220px; }
  .status-right { justify-content: flex-end; }
  .status-time { font-weight: 600; }
  .signal-dots { display: flex; gap: 3px; }
  .signal-dots span { width: 11px; height: 11px; border-radius: 50%; border: 1.5px solid var(--text-light); }
  .signal-dots span.on { background: var(--text-light); }
  .battery { width: 48px; height: 20px; border: 2px solid var(--text-light); border-radius: 4px; padding: 2px; position: relative; }
  .battery::after { content: ""; position: absolute; right: -6px; top: 5px; width: 3px; height: 7px; background: var(--text-light); border-radius: 0 2px 2px 0; }
  .battery i { display: block; width: 100%; height: 100%; background: var(--text-light); border-radius: 1px; }

  .here-label {
    position: absolute; top: 112px; width: 100%;
    text-align: center; color: var(--accent);
    font-size: 24px; letter-spacing: 0.5px;
  }
  .coordinates {
    position: absolute; top: 164px; width: 100%;
    text-align: center; color: var(--accent);
    font-size: 70px; font-weight: 700; line-height: 82px;
  }
  .precision {
    position: absolute; top: 352px; width: 100%;
    text-align: center; color: var(--muted);
    font-size: 18px;
  }
  .action-list {
    position: absolute; left: 186px; top: 446px;
    width: 370px; display: flex; flex-direction: column; gap: 33px;
  }
  .action-button {
    height: 75px;
    border: 3px solid var(--button-border);
    border-radius: 5px;
    background: var(--button-fill);
    display: flex; align-items: center;
    color: var(--text-light);
    font-weight: 600;
    text-decoration: none;
  }
  .action-icon { width: 98px; display: flex; justify-content: center; }
  .action-text { font-size: 27px; }
  .action-text.small { font-size: 21px; }

  .map-area {
    position: absolute; left: 0; right: 0; bottom: 0; height: 406px;
    background: linear-gradient(100deg, var(--map-land) 0%, var(--map-forest) 40%, var(--map-forest) 70%, var(--map-land) 100%);
  }
  .map-marker { position: absolute; left: 290px; top: 189px; }
</style>
</head>
<body>
<main class="app-screen">
  <section class="location-panel">
    <header class="status-bar">
      <div class="status-left">
        <div class="signal-dots"><span class="on"></span><span class="on"></span><span class="on"></span><span></span><span></span></div>
        <span class="carrier">KESTREL</span>
        <svg width="24" height="18" viewBox="0 0 24 18" aria-hidden="true"><path d="M2 6a14 14 0 0 1 20 0M5.5 9.5a9 9 0 0 1 13 0M9 13a4 4 0 0 1 6 0" fill="none" stroke="#f2f5f5" stroke-width="2.4" stroke-linecap="round"/><circle cx="12" cy="16" r="1.8" fill="#f2f5f5"/></svg>
      </div>
      <span class="status-time">4:21 PM</span>
      <div class="status-right">
        <svg width="14" height="22" viewBox="0 0 14 22" aria-hidden="true"><path d="M2 6l10 9-5 5V2l5 5-10 9" fill="none" stroke="#9aa9ab" stroke-width="1.8"/></svg>
        <span>100%</span>
        <div class="battery"><i></i></div>
      </div>
    </header>

    <p class="here-label">YOU ARE HERE</p>
    <h1 class="coordinates">40 25.56 N°<br>82 55.62 W°</h1>
    <p class="precision">(PRECISION 10 METERS)</p>

    <nav class="action-list">
      <a class="action-button" href="tel:911">
        <span class="action-icon">
          <svg width="34" height="34" viewBox="0 0 34 34" aria-hidden="true"><path d="M8 4l5 6-3 3c1.5 4 5 7.5 9 9l3-3 6 5-3 5C14 28 6 20 5 7z" fill="#f2f5f5"/><path d="M20 8a7 7 0 0 1 6 6M20 3a12 12 0 0 1 11 11" fill="none" stroke="#f2f5f5" stroke-width="2" stroke-linecap="round"/></svg>
        </span>
        <span class="action-text">CALL FOR HELP</span>
      </a>
      <a class="action-button" href="#first-aid">
        <span class="action-icon">
          <svg width="30" height="26" viewBox="0 0 30 26" aria-hidden="true"><rect x="10" y="1" width="10" height="6" rx="1.5" fill="none" stroke="#f2f5f5" stroke-width="2.4"/><rect x="1" y="6" width="28" height="19" rx="3" fill="#f2f5f5"/><path d="M15 10v11M9.5 15.5h11" stroke="#23434a" stroke-width="3.5"/></svg>
        </span>
        <span class="action-text">FIRST AID TIPS</span>
      </a>
      <a class="action-button" href="#landing-zone">
        <span class="action-icon">
          <svg width="48" height="28" viewBox="0 0 48 28" aria-hidden="true"><path d="M8 3h32M24 3v5" stroke="#f2f5f5" stroke-width="2.4" stroke-linecap="round"/><path d="M16 8h14c6 0 10 4 10 8v2H20L16 14z" fill="#f2f5f5"/><path d="M16 12H3M3 8v8" stroke="#f2f5f5" stroke-width="2.4" stroke-linecap="round"/><path d="M32 11h5v4h-5z" fill="#23434a"/><path d="M20 24h24M26 19v5M36 19v5" stroke="#f2f5f5" stroke-width="2" stroke-linecap="round"/></svg>
        </span>
        <span class="action-text small">LANDING ZONE GUIDE</span>
      </a>
    </nav>
  </section>

  <section class="map-area" role="img" aria-label="Road map of the surrounding forest region with the caller's position marked">
    <svg class="map-marker" width="160" height="150" viewBox="0 0 160 150" aria-hidden="true">
      <circle cx="80" cy="75" r="70" fill="rgba(232,69,60,0.12)" stroke="#e8453c" stroke-width="1.5" stroke-opacity="0.6"/>
      <circle cx="80" cy="75" r="48" fill="none" stroke="#e8453c" stroke-width="4"/>
      <path d="M80 88c-6-11-12-17-12-24a12 12 0 0 1 24 0c0 7-6 13-12 24z" fill="#e8453c" stroke="#a9231c" stroke-width="1.2"/>
      <circle cx="80" cy="63" r="3.5" fill="#7d1812"/>
    </svg>
  </section>
</main>
</body>
</html>
```